Start-up Cleaning Business Needs Professional Business Cards

Marta's Butler Cleaning, LLC, is a start-up business based in the Northern Virginia suburbs of Washington, DC. MBC provides cleaning and housekeeping services for homes and offices. We have three core values:

1. We are personal. We value knowing and being known by our customers and each other. If you want nameless, faceless service, you should choose another provider. We put "personal" at the front of the list, because it is most important to us; the design we choose will convey this value.

2. Like a hotel concierge, we are professional in attitude, posture, communication and processes.

3. Like a hotel concierge, we solve problems with a can-do attitude and never make excuses.

Our uniforms are khaki pants with pink polo shirts.

Our logo is attached. There are other symbols, not represented in our logo, that may convey our values well, such as a top hat and bow tie, magnifying glass, desk bell, etc.

Please include fields for an individual's name and title, office phone number, mobile phone number, email address and website address (www.martasbutlercleaning.example).

Standard U.S. size: 2" x 3.5"
Updates

I should have mentioned that the purpose of all our advertising - business cards included - is to motivate potential customers to call or email to arrange a free in-home estimate.

```html
<!DOCTYPE html>
<html lang="en">
<head>
<meta charset="utf-8">
<title>Marta's Butler Cleaning – Business Card</title>
<link href="https://fonts.googleapis.com/css2?family=Open+Sans:wght@400;600;700&display=swap" rel="stylesheet">
<style>
  :root {
    --page-bg: #e9e9ee;
    --card-white: #ffffff;
    --band-charcoal: #3c3c3c;
    --band-pink: #ec3d97;
    --ink-grey: #5a5a5a;
    --text-light: #ffffff;
    --art-pink: #f2a6cc;
    --art-brown: #c9b2ad;
  }
  * { margin: 0; padding: 0; box-sizing: border-box; }
  html, body { width: 1200px; height: 987px; overflow: hidden; }
  body {
    background: var(--page-bg);
    font-family: "Open Sans", Arial, sans-serif;
    position: relative;
  }
  .card {
    position: absolute;
    left: 250px;
    width: 700px;
    height: 400px;
    background: var(--card-white);
    border-radius: 28px;
    overflow: hidden;
    box-shadow: 0 6px 18px rgba(0,0,0,0.12);
  }
  .card--back { top: 55px; }
  .card--front { top: 532px; }

  .mascot-art {
    position: absolute;
    border-radius: 18px;
    background: linear-gradient(135deg, var(--art-brown), var(--art-pink));
  }
  .card--back .mascot-art { left: 270px; top: 80px; width: 170px; height: 170px; }
  .back-website {
    position: absolute;
    left: 0; right: 0; top: 285px;
    text-align: center;
    font-size: 20px;
    letter-spacing: 1px;
    color: var(--ink-grey);
  }

  .card--front .mascot-art { left: 300px; top: 18px; width: 100px; height: 100px; }
  .brand-name {
    position: absolute;
    left: 0; right: 0; top: 122px;
    text-align: center;
    font-size: 26px;
    font-weight: 400;
    color: var(--ink-grey);
  }
  .band-charcoal {
    position: absolute;
    left: 0; right: 0; top: 172px; height: 160px;
    background: var(--band-charcoal);
  }
  .band-pink {
    position: absolute;
    left: 0; right: 0; bottom: 0; height: 68px;
    background: var(--band-pink);
    color: var(--text-light);
    font-weight: 600;
    font-size: 24px;
    letter-spacing: 0.5px;
    display: flex; align-items: center;
    padding-left: 60px;
  }
  .person {
    position: absolute;
    right: 420px; top: 30px;
    text-align: right;
    color: var(--text-light);
  }
  .person__name { font-size: 26px; font-weight: 700; line-height: 1.2; }
  .person__title { font-size: 20px; }
  .divider {
    position: absolute;
    left: 300px; top: 28px; width: 1px; height: 100px;
    background: #8a8a8a;
  }
  .contacts {
    position: absolute;
    left: 320px; top: 24px;
    list-style: none;
    color: var(--text-light);
    font-size: 21px;
  }
  .contacts li { display: flex; align-items: center; gap: 10px; height: 36px; }
  .contacts svg { width: 22px; height: 22px; flex: none; }
</style>
</head>
<body>

  <section class="card card--back" aria-label="Card back">
    <div class="mascot-art" role="img" aria-label="Illustration of a cleaner in pink sweeping with a mop"></div>
    <p class="back-website">www.Martas.example</p>
  </section>

  <section class="card card--front" aria-label="Card front">
    <div class="mascot-art" role="img" aria-label="Illustration of a cleaner in pink sweeping with a mop"></div>
    <p class="brand-name">Marta's</p>

    <div class="band-charcoal">
      <div class="person">
        <p class="person__name">Your Name</p>
        <p class="person__title">Title</p>
      </div>
      <span class="divider"></span>
      <ul class="contacts">
        <li>
          <svg viewBox="0 0 24 24"><circle cx="12" cy="12" r="11" fill="none" stroke="#fff" stroke-width="1.6"/><path d="M8 6.5c.6-.4 1.3-.3 1.6.3l1 2c.2.5 0 1-.4 1.3l-.7.5c.6 1.4 1.6 2.5 3 3.1l.5-.7c.3-.4.9-.6 1.3-.3l2 1c.6.3.7 1 .3 1.6-.8 1-2 1.5-3.3 1-3-1.1-5.3-3.4-6.3-6.4-.4-1.3 0-2.6 1-3.4z" fill="#fff"/></svg>
          012-345-6789
        </li>
        <li>
          <svg viewBox="0 0 24 24"><rect x="2" y="5" width="20" height="14" rx="2" fill="#fff"/><path d="M3 6l9 7 9-7" fill="none" stroke="#3c3c3c" stroke-width="1.6"/></svg>
          Info@Martas.example
        </li>
        <li>
          <svg viewBox="0 0 24 24" fill="none" stroke="#fff" stroke-width="1.6"><circle cx="12" cy="12" r="10"/><ellipse cx="12" cy="12" rx="4.5" ry="10"/><path d="M2 12h20M4 7h16M4 17h16"/></svg>
          www.Martas.example
        </li>
      </ul>
    </div>

    <div class="band-pink">Marta's Butler Cleaning, LLC</div>
  </section>

</body>
</html>
```